Stationary for Wealth Management Firm

We need stationary design based on our new business cards. We would like it to be simple, clean and understated. A lot of our clients are seniors so the fonts cannot be too small. Our colors are dark blue and light grey.

This is what we need:

1. Letterhead US Letter – 8.5" x 11" CMYK 300 DPI
2. Invoice US Letter – 8.5" x 11" CMYK 300 DPI
3. Fax Cover Sheet US Letter – 8.5" x 11" CMYK 300 DPI
4. Email Signature

Including: logo, motto, address with phone and fax numbers, web address, and compliance disclosure.

5. Standard Envelope #10 – 9,5” x 4,125” CMYK 300 Dpi
6. Large Envelope – 9” x 12” CMYK 300 Dpi

Including: logo, motto, addresses without phone and fax numbers, web address, and compliance disclosure.

7. Letterhead Follower US Letter – 8.5" x 11" CMYK 300 DPI

Including: logo, motto, and web address.

8. Flat Invitation Cards – 6” x 4” CMYK 300 Dpi
9. Pocket Folder – 9" x 12”, CMYK 300 Dpi

Including: logo and motto.

Here is the info:

Company: Harrowmere Wealth Management LLC
Address 1: 4715 Lantern Ave. Suite K-12, Ashford Mills, OH, 44907
Phone 1: 1-215-555-0172
Address 2: 618 Fenwick Circle, New London Twp., PA, 19352
Phone 2: 1-610-555-0139
Fax: 1-484-555-0196
Motto: Steady Hands Since Day One (in grey #A8A8A8 and US Declaration font)
Web address: www.harrowmerewealth.example
Compliance disclosure: Securities and Advisory Services offered through QVR Capital. Member NASTO/CUDA.
Logo: in uploaded files

Industry/Entity Type

Business

Requirements
Must have
• Need to blend the business card look and feel with the brochure/website look and feel.

```html
<!DOCTYPE html>
<html lang="en">
<head>
<meta charset="utf-8">
<title>Harrowmere Wealth Management – Stationery</title>
<link rel="stylesheet" href="https://fonts.googleapis.com/css2?family=Cinzel:wght@400&family=Open+Sans:wght@400&display=swap">
<style>
  :root {
    --navy: #1c2454;
    --navy-mid: #2d3462;
    --navy-light: #5d6290;
    --lavender: #c8c8db;
    --lavender-faint: #e4e4ee;
    --paper: #ffffff;
    --backdrop: #ececec;
    --ink: #2e2e38;
    --rule: #b9b9c8;
  }
  html, body { margin: 0; padding: 0; overflow: hidden; }
  body {
    width: 1200px; height: 1111px; position: relative;
    background: var(--backdrop);
    font-family: "Open Sans", Arial, sans-serif;
    color: var(--ink);
  }
  .sheet { position: absolute; background: var(--paper); overflow: hidden; box-shadow: 0 2px 6px rgba(0,0,0,.12); }
  .sheet svg.art { position: absolute; left: 0; top: 0; }
  .brand { position: absolute; font-family: "Cinzel", Georgia, serif; color: var(--navy); line-height: 1; white-space: nowrap; }
  .brand-mark { display: inline-block; background: var(--navy); vertical-align: top; }
  .brand-name { display: block; letter-spacing: .02em; }
  .brand-sub { display: block; font-family: "Open Sans", Arial, sans-serif; letter-spacing: .04em; }
  .brand.on-dark { color: #ffffff; }
  .brand.on-dark .brand-mark { background: #ffffff; }

  /* Letterhead */
  .letterhead { left: 123px; top: 135px; width: 421px; height: 588px; }
  .letterhead .brand { left: 40px; top: 28px; }
  .letterhead .brand-mark { width: 18px; height: 18px; margin-bottom: 8px; }
  .letterhead .brand-name { font-size: 15px; }
  .letterhead .brand-sub { font-size: 7px; margin-top: 2px; }
  .letterhead .contact { position: absolute; left: 279px; top: 40px; width: 138px; font-size: 6.2px; line-height: 1.4; color: var(--navy); }
  .letter-body { position: absolute; left: 40px; top: 116px; width: 360px; font-size: 7.2px; line-height: 1.45; }
  .letter-body p { margin: 0 0 10px; }
  .letter-body .closing-gap { margin-top: 26px; }
  .letterhead .foot-rule { position: absolute; left: 40px; right: 36px; top: 568px; border-top: 1px solid var(--rule); }

  /* Pocket folder */
  .folder { left: 603px; top: 112px; width: 495px; height: 627px; background: linear-gradient(100deg, var(--navy-mid) 0%, var(--navy-light) 100%); }
  .folder .brand { left: 223px; top: 279px; }
  .folder .brand-mark { width: 20px; height: 20px; margin-bottom: 14px; }
  .folder .brand-name { font-size: 15px; }
  .folder .brand-sub { font-size: 7px; margin-top: 2px; }

  /* Envelopes */
  .envelope { top: 781px; height: 230px; }
  .envelope-front { left: 123px; width: 480px; }
  .envelope-back { left: 624px; width: 485px; }
  .envelope .brand { left: 38px; top: 22px; }
  .envelope .brand-mark { width: 16px; height: 16px; margin-bottom: 6px; }
  .envelope .brand-name { font-size: 10.5px; }
  .envelope .brand-sub { font-size: 5px; margin-top: 1px; }
  .envelope-back .brand { left: 40px; top: 26px; }
  .envelope-back .brand-mark { width: 12px; height: 12px; margin-bottom: 5px; }
  .envelope-back .brand-name { font-size: 8px; }
  .envelope-back .brand-sub { font-size: 4px; }
  .envelope .contact-line { position: absolute; left: 38px; top: 198px; font-size: 5.6px; color: var(--navy); white-space: nowrap; }
  .envelope .foot-rule { position: absolute; left: 38px; right: 20px; top: 208px; border-top: 1px solid var(--rule); }
</style>
</head>
<body>

<section class="sheet letterhead" aria-label="Letterhead">
  <svg class="art" width="421" height="588" viewBox="0 0 421 588">
    <polygon points="0,0 300,0 0,56" fill="var(--lavender)"/>
    <rect x="40" y="28" width="230" height="32" fill="var(--lavender-faint)" role="img" aria-label="Brand column decoration band"/>
  </svg>
  <div class="brand">
    <span class="brand-mark"></span>
    <span class="brand-name">HARROWMERE</span>
    <span class="brand-sub">WEALTH MANAGEMENT</span>
  </div>
  <div class="contact">Company: Harrowmere Wealth Management LLC | Address 1: 4715 Lantern Ave. Suite K-12, Ashford Mills, OH, 44907 | Phone 1: 1-215-555-0172</div>
  <div class="letter-body">
    <p>1820, Quarry Ridge Street<br>Marston Bay, OR 97999.</p>
    <p>January 29th, 2011</p>
    <p>Mr. Pellham<br>President, Pellham Children's Center<br>517 Marlow Lane<br>Dunmere Falls, VT 05999</p>
    <p>Dear Mr. Pellham:</p>
    <p>In the first paragraph, one needs to give a brief introduction of oneself. One should also give reference to the purpose of the letter in brief.<br>The second paragraph needs to give the details of the letter and its need. This paragraph is mostly longer than the others and plays the main role in the letter. Keep the sentences short and to the point. Avoid using complex words and sentences.</p>
    <p class="closing-gap">The third and last paragraph is the conclusion of the letter and can be kept short.</p>
    <p>Sincerely,</p>
    <p>(this is where the signature of the writer will be placed)</p>
    <p>Dana Whitlock<br>Read more at Letterworks: http://www.letterworks.example/articles/letter-format.html</p>
  </div>
  <div class="foot-rule"></div>
</section>

<section class="sheet folder" aria-label="Pocket folder">
  <svg class="art" width="495" height="627" viewBox="0 0 495 627">
    <polygon points="0,363 495,248 495,627 0,627" fill="var(--navy)"/>
    <rect x="223" y="300" width="240" height="327" fill="#ffffff" opacity="0.08" role="img" aria-label="Faint brand column decoration"/>
  </svg>
  <div class="brand on-dark">
    <span class="brand-mark"></span>
    <span class="brand-name">HARROWMERE</span>
    <span class="brand-sub">WEALTH MANAGEMENT</span>
  </div>
</section>

<section class="sheet envelope envelope-front" aria-label="Envelope front">
  <svg class="art" width="480" height="230" viewBox="0 0 480 230">
    <polygon points="0,0 270,0 0,42" fill="var(--lavender)"/>
    <rect x="38" y="24" width="180" height="206" fill="var(--lavender-faint)" role="img" aria-label="Brand column decoration band"/>
  </svg>
  <div class="brand">
    <span class="brand-mark"></span>
    <span class="brand-name">HARROWMERE</span>
    <span class="brand-sub">WEALTH MANAGEMENT</span>
  </div>
  <div class="contact-line">Company: Harrowmere Wealth Management LLC | Address 1: 4715 Lantern Ave. Suite K-12, Ashford Mills, OH, 44907 | Phone 1: 1-215-555-0172</div>
  <div class="foot-rule"></div>
</section>

<section class="sheet envelope envelope-back" aria-label="Envelope back">
  <svg class="art" width="485" height="230" viewBox="0 0 485 230">
    <rect x="40" y="36" width="200" height="194" fill="var(--lavender-faint)" role="img" aria-label="Brand column decoration band"/>
    <polygon points="0,0 485,0 485,30 0,62" fill="var(--lavender-faint)"/>
    <polygon points="0,0 485,0 0,20" fill="var(--lavender)"/>
    <line x1="0" y1="62" x2="485" y2="30" stroke="var(--rule)" stroke-width="1"/>
  </svg>
  <div class="brand">
    <span class="brand-mark"></span>
    <span class="brand-name">HARROWMERE</span>
    <span class="brand-sub">WEALTH MANAGEMENT</span>
  </div>
  <div class="foot-rule"></div>
</section>

</body>
</html>
```